Patient Recruitment Presentation for a Clinical Trial

We need a powerpoint designed to recruit patients for a clinical trial. We need 4 slides designed: an opening slide, two body slides, and an end slide. The opening slide should include the question, "Do you suffer from Depression?" in the middle of the screen, but other than that just include the design, graphic, or texture that you develop. The 2 body slides should allow for the title of study (please use “Depression Research Study”) to be across the top and contact information (phone number, URL) to be on the bottom of the slide, either centered or left or right justified. Whether this text (study title and contact information) is set off by a banner or shape that stretches across the entire slide or just provides a background to that text is up to you. One of the two body slides should include the attached horizontal stock image with a clear section to insert text either beside or over the top of the negative space of the image. This image should be stretch to the full width of the screen. The second body slide should include the attached vertical stock image, with a clear section to insert text beside the picture. (You can crop vertical portions of the images if needed.)

The end slide should resemble the opening slide in terms of design, yet this time includes the study title and contact information prominently displayed.

In terms of design, we’re looking for something clean and trustworthy, and even though this is medical, we don’t want any pills, test tubes, or heart rate lines. We’re trying to give people hope, so we want to earn their trust by communicating quality and excellence.

Please see the attached examples of the types of designs and layouts we like, how the images need to be treated, and places for text need to be designed.

We need the design to be 1920x1080 pixels, and we need the slides delivered as layered PSD files so we can manipulate as needed.

Thanks!

Target Market(s)

Adults in the US that are not working full time and able to participate in a research study.

Industry/Entity Type

Medical

Font styles to use
Serif
Sans Serif

Requirements
Must have
• The design must use the two images attached as specified in the brief. Other than that, I'm open to your creative interpretation.
Nice to have
• Nice clean design, clean fonts, nice color palette.
Should not have
• Images or designs relating to the medical world, no test tubes, heart rate lines, images of doctors or pills, etc.

```html
<!DOCTYPE html>
<html lang="en">
<head>
<meta charset="utf-8">
<title>Depression Research Study</title>
<link rel="stylesheet" href="https://fonts.googleapis.com/css2?family=Source+Sans+3:wght@400&display=swap">
<style>
  :root {
    --banner: #00b5e6;
    --banner-text: #ffffff;
    --body-text: #0f4f5c;
    --panel: rgba(240, 236, 232, 0.72);
    --photo-light: #e9e4de;
    --photo-mid: #c9b9ad;
    --photo-skin: #8f5f4a;
    --photo-dark: #3a2e2a;
    --edge: #2a3a44;
  }
  * { margin: 0; padding: 0; box-sizing: border-box; }
  html, body { width: 1200px; height: 675px; overflow: hidden; }
  body { font-family: "Source Sans 3", "Myriad Pro", Arial, sans-serif; background: #ffffff; }
  .slide { position: relative; width: 1200px; height: 675px; overflow: hidden; }
  .slide-photo {
    position: absolute; inset: 0;
    background:
      radial-gradient(ellipse 260px 340px at 880px 360px, var(--photo-skin) 0%, rgba(143,95,74,0.6) 45%, rgba(143,95,74,0) 75%),
      radial-gradient(ellipse 300px 200px at 900px 20px, var(--photo-dark) 0%, rgba(58,46,42,0) 80%),
      radial-gradient(ellipse 260px 180px at 960px 640px, #dfe6ee 0%, rgba(223,230,238,0) 80%),
      linear-gradient(90deg, var(--edge) 0, #6d7a80 22px, var(--photo-light) 60px, var(--photo-mid) 560px, #b9a79b 700px, #d8d4d2 1200px);
  }
  .text-panel {
    position: absolute; left: 20px; top: 0; width: 634px; height: 675px;
    background: var(--panel);
  }
  .title-banner {
    position: absolute; left: 20px; top: 45px; width: 1180px; height: 127px;
    background: var(--banner);
    display: flex; align-items: center; justify-content: center;
  }
  .study-title {
    color: var(--banner-text); font-weight: 400; font-size: 68px;
    text-transform: uppercase; letter-spacing: 0.5px; line-height: 1;
    white-space: nowrap;
  }
  .study-summary {
    position: absolute; left: 90px; top: 212px; width: 516px;
    color: var(--body-text); font-size: 50px; line-height: 73px;
    letter-spacing: -0.6px; text-align: justify;
  }
  .contact-strip {
    position: absolute; left: 20px; top: 604px; width: 1180px; height: 52px;
    background: var(--banner);
    display: flex; align-items: center; justify-content: center; gap: 64px;
    color: var(--banner-text); font-size: 28px; line-height: 1;
  }
</style>
</head>
<body>
  <main class="slide">
    <div class="slide-photo" role="img" aria-label="Stock photo of a thoughtful woman resting her head on her hand, softly lit indoors"></div>
    <div class="text-panel"></div>
    <header class="title-banner">
      <h1 class="study-title">Depression Research Study</h1>
    </header>
    <p class="study-summary">Lorem ipsum dolor sit amet, consectetuer adipiscing elit, sed diam nonummy nibh euismod tincidunt</p>
    <footer class="contact-strip">
      <span class="contact-phone">(555) 010-2468</span>
      <span class="contact-url">www.depressionstudy.example</span>
    </footer>
  </main>
</body>
</html>
```